KORVa: AI driven decarbonization application

We are seeking an engaging, user-friendly, and visually appealing user interface for our B2B SaaS platform, Brelmont KORVa. This solution helps large organizations achieve net-zero emissions using AI-driven forecasting, AI models, a emission mitigation library, and a scenario simulator..

A big challenge is to allow the user to work efficiently with multidimensional data.

Requirements:

* Design a modern, professional, and visually striking user interface, catering to a diverse audience within large corporations, including executives, strategists, and environmental specialists.

* Construct an intuitive navigation system, allowing users to seamlessly access functionalities for informed decision-making and tracking progress towards net-zero emissions.

* The application is expected to be used on desktops first

* Incorporate our brand's colors, and visual elements into the design to maintain consistency throughout the application.

* Provide design assets and documentation, such as style guides, design specifications, and necessary assets (e.g., icons, illustrations) for our development team to implement the design. We use Figma and would appreciate delivery as figma files.

Please note that we also need more pages over time. The most important is to get the work bench page right. We will also need:
* a landing page where the users can select previous scenarios and see some high level data.
* A page with information on historical data per asset
* An analytics page
* User and system administration pages.
These pages are out of scope for this project, but they should be available in the navigation solution.

Please submit your initial design concepts, accompanied by a brief explanation of your approach and the rationale behind your design choices. We will offer feedback and collaborate with the chosen designer to refine the design, ensuring it meets our requirements and vision.

We are really hoping to see some elegant user interfaces. The functionality describe in the attachment is important, but the layout is not. Feel free to invent.

Attached files:

Target Market(s)

Energy intensive industries

Requirements
Must have
• Easy to navigate through the different data dimensions: Time, assets, mitigation measures, and advanced details under mitigation measures. The design in the attached files are just our working drafts. Creative alternatives are very welcome.
Nice to have
• Elegant layouts that differ from our working drafts.

```html
<!DOCTYPE html>
<html lang="en">
<head>
<meta charset="utf-8">
<title>Brelmont KORVa – Workbranch</title>
<link rel="stylesheet" href="https://fonts.googleapis.com/css2?family=Inter:wght@400;500;600;700;800&display=swap">
<style>
:root{
  --bg-top:#3a3a3a;
  --bg-bottom:#231f1e;
  --navy:#0f4673;
  --navy-logo:#14568f;
  --navy-text:#0f4673;
  --side-bg:#f1f7fd;
  --row-hi:#e4f0fb;
  --panel:#f7fafd;
  --white:#ffffff;
  --ink:#1c2733;
  --muted:#8a939c;
  --grey-bar:#e6e9ee;
  --tick-green:#1aa37a;
  --tick-grey:#a2a9b0;
  --gold:#dfa21f;
  --purple:#9b6bb5;
  --teal:#5c9896;
  --red:#e56a7a;
  --band:#ecf5fd;
  --timeline:#eef2f7;
  --grid:#d9dee5;
}
*{box-sizing:border-box;margin:0;padding:0}
html,body{width:1200px;height:896px;overflow:hidden}
body{background:linear-gradient(180deg,var(--bg-top),var(--bg-bottom));font-family:'Inter',sans-serif;color:var(--ink)}
.stage{position:absolute;left:0;top:0;width:1597px;height:1192px;transform:scale(0.7514);transform-origin:0 0}
.app{position:absolute;left:78px;top:138px;width:1440px;height:914px;border-radius:12px;overflow:hidden;background:var(--white)}
.abs{position:absolute}

/* top bar */
.topbar{left:0;top:0;width:1440px;height:56px;background:var(--navy)}
.brand{left:0;top:0;width:359px;height:56px;background:var(--navy-logo);display:flex;align-items:center;justify-content:center;gap:8px;color:#fff;font-size:21px;font-weight:500;letter-spacing:2px}
.brand .dot{width:9px;height:9px;border-radius:50%;background:#fff}
.nav{left:384px;top:0;height:56px;display:flex;align-items:center;gap:33px;color:#fff;font-size:16px}
.nav .current{font-weight:700}
.nav .alert{position:relative}
.nav .alert::after{content:"";position:absolute;right:-7px;top:-4px;width:9px;height:9px;border-radius:50%;background:#e4432c}
.quick{left:1066px;top:0;height:56px;display:flex;align-items:center;gap:10px;color:#fff;font-size:16px}
.user{left:1257px;top:0;height:56px;display:flex;align-items:center;gap:10px;color:#fff;font-size:16px}
.gear{left:1376px;top:13px;width:30px;height:30px;border-radius:50%;background:#2c6394;display:flex;align-items:center;justify-content:center}

/* sidebar */
.sidebar{left:0;top:56px;width:359px;height:858px;background:var(--white)}
.lib-head{left:0;top:0;width:359px;height:114px;background:var(--side-bg)}
.lib-title{left:29px;top:15px;font-size:16px;font-weight:800;color:var(--navy-text)}
.collapse{left:325px;top:19px}
.search{left:50px;top:53px;width:232px;height:40px;border-radius:20px;background:#e0ecf7;display:flex;align-items:center;gap:14px;padding-left:18px;color:#5e7184;font-size:16px}
.filter{left:290px;top:53px;width:40px;height:40px;border-radius:50%;background:#e0ecf7;display:flex;align-items:center;justify-content:center}
.group{position:absolute;left:0;width:359px;height:37px;background:var(--navy);color:#fff;display:flex;align-items:center;padding-left:32px;font-size:14.5px}
.group .applied{position:absolute;right:57px;font-size:12.5px;color:#c9dbee}
.group svg{position:absolute;right:34px}
.measure{position:absolute;left:0;width:359px;height:33px;display:flex;align-items:center;padding-left:48px;font-size:14.5px;color:#7c858e}
.measure.on{background:var(--row-hi);color:var(--ink)}
.measure .count{position:absolute;right:77px;font-size:12.5px;color:#a8b0b8}
.measure.on .count{color:var(--navy-text)}
.measure .box{position:absolute;right:50px;width:12px;height:12px;border-radius:2px;background:#dfe4e9}
.measure .box::after{content:"";position:absolute;left:3px;top:5px;width:6px;height:2px;background:#fff}
.measure.on .box{background:#3f6c88}

/* assets */
.assets{left:359px;top:56px;width:492px;height:595px;background:var(--panel)}
.panel-title{font-size:16px;font-weight:800;color:var(--navy-text)}
.asset-row{position:absolute;left:32px;width:428px;height:20px;font-size:12px;display:flex;align-items:center}
.asset-row span{position:absolute}
.tick{position:absolute;width:14px;height:14px}
.adv-bar{left:0;top:317px;width:492px;height:36px;background:var(--grey-bar);display:flex;align-items:center;padding-left:32px;font-size:12.5px;font-weight:700;color:var(--navy-text)}
.setting{position:absolute;left:32px;width:428px;height:20px;font-size:12px;display:flex;align-items:center;color:#a1a8b0}
.setting.live{color:var(--ink)}
.setting .state{position:absolute;right:28px}
.setting.live .state{color:var(--tick-green)}

/* simulation */
.sim{left:851px;top:56px;width:589px;height:595px;background:var(--white)}
.view-btn{position:absolute;top:13px;width:32px;height:32px;border-radius:50%;background:#e8eef4;display:flex;align-items:center;justify-content:center}
.view-btn.on{background:var(--navy)}
.legend{position:absolute;left:78px;top:75px;display:flex;gap:28px;font-size:12.5px;color:#1f5b8c}
.legend i{display:inline-block;width:8px;height:8px;border-radius:50%;margin-right:7px}
.chart{position:absolute;left:0;top:0}
.axis-label{font-family:'Inter',sans-serif;font-size:11px;fill:#1f4d75}

/* timeline */
.timeline{left:359px;top:651px;width:1081px;height:263px;background:var(--timeline)}
.year{position:absolute;top:11px;font-size:12.5px;color:#27435c;transform:translateX(-50%)}
.gridline{position:absolute;top:32px;width:1px;height:231px;background:var(--grid)}
.plan{position:absolute;height:37px;display:flex;align-items:center;padding-left:12px;color:#fff;font-size:14.5px}
.plan .modify{position:absolute;right:14px;display:flex;align-items:center;gap:10px;font-size:12.5px}
.plan .modify b{width:12px;height:10px;border-radius:2px;background:#fff;display:inline-block;position:relative}
.plan .modify b::after{content:"";position:absolute;left:4px;top:3px;width:4px;height:4px;border-radius:50%;background:currentColor}
.plan.gold{background:var(--gold);color:#fff}
.plan.purple{background:var(--purple)}
.plan.teal{background:var(--teal)}
.plan .modify b::after{background:inherit}
.switch{left:744px;top:203px;width:314px;height:35px;border-radius:18px;background:#fff;overflow:hidden;display:flex;box-shadow:0 1px 3px rgba(0,0,0,.08)}
.switch div{flex:1;display:flex;align-items:center;justify-content:center;gap:10px;font-size:12.5px;letter-spacing:.5px}
.switch .pick{color:#0f4673}
.switch .active{background:var(--navy);color:#fff;border-radius:18px 18px 18px 0}
</style>
</head>
<body>
<div class="stage">
<div class="app">

  <header class="abs topbar">
    <div class="abs brand"><span class="dot"></span>Brelmont</div>
    <nav class="abs nav">
      <span>Home</span><span>Assets</span><span class="current">Workbranch</span><span class="alert">Simulation</span><span>Map</span>
    </nav>
    <div class="abs quick">Quick Actions
      <svg width="18" height="22" viewBox="0 0 18 22"><path d="M11 1 3 12h6l-2 9 8-12H9l2-8z" fill="none" stroke="#fff" stroke-width="1.6" stroke-linejoin="round"/></svg>
    </div>
    <div class="abs user">Alex Moren
      <svg width="12" height="8" viewBox="0 0 12 8"><path d="M1 1l5 5 5-5z" fill="#fff"/></svg>
    </div>
    <div class="abs gear">
      <svg width="18" height="18" viewBox="0 0 24 24" fill="none" stroke="#fff" stroke-width="1.8"><circle cx="12" cy="12" r="3"/><path d="M12 2l2 3 3.5-.8.8 3.5 3 2-2 3 .8 3.5-3.5.8-2 3-3-2-3 2-2-3-3.5-.8.8-3.5-2-3 3-2 .8-3.5L10 5z" stroke-linejoin="round"/></svg>
    </div>
  </header>

  <aside class="abs sidebar">
    <div class="abs lib-head">
      <h2 class="abs lib-title">MEASURES LIBRARY</h2>
      <svg class="abs collapse" width="18" height="18" viewBox="0 0 18 18"><rect x="1" y="1" width="16" height="16" rx="1" fill="none" stroke="#0f4673" stroke-width="2"/><rect x="1" y="1" width="6" height="16" fill="#0f4673"/><path d="M13 5l-4 4 4 4z" fill="#0f4673"/></svg>
      <div class="abs search">
        <svg width="20" height="20" viewBox="0 0 20 20"><circle cx="8" cy="8" r="6" fill="none" stroke="#4d6a87" stroke-width="2"/><path d="M12.5 12.5 18 18" stroke="#4d6a87" stroke-width="2.2" stroke-linecap="round"/></svg>
        Search measures
      </div>
      <div class="abs filter"><svg width="18" height="18" viewBox="0 0 18 18"><path d="M1 2h16l-6 7v7l-4-2V9z" fill="#4d6a87"/></svg></div>
    </div>

    <div class="group" style="top:114px">Switch Energy Carrier<span class="applied">1 Applied</span><svg width="12" height="8" viewBox="0 0 12 8"><path d="M0 0h12L6 7z" fill="#fff"/></svg></div>
    <div class="measure" style="top:151px">Ammonium<span class="count">0/0</span><span class="box"></span></div>
    <div class="measure on" style="top:184px">Biodiesel<span class="count">20/28</span><span class="box"></span></div>
    <div class="measure" style="top:217px">Ethanol<span class="count">0/0</span><span class="box"></span></div>
    <div class="measure" style="top:250px">Hydrogen<span class="count">0/0</span><span class="box"></span></div>
    <div class="measure" style="top:283px">LNG<span class="count">0/0</span><span class="box"></span></div>
    <div class="measure" style="top:316px">Methanol<span class="count">0/0</span><span class="box"></span></div>
    <div class="measure" style="top:349px">Power from offshore wind<span class="count">0/0</span><span class="box"></span></div>
    <div class="measure" style="top:382px">Power from shore<span class="count">0/0</span><span class="box"></span></div>

    <div class="group" style="top:419px">Energy efficiency Measures<span class="applied">2&nbsp; Applied</span><svg width="12" height="8" viewBox="0 0 12 8"><path d="M0 0h12L6 7z" fill="#fff"/></svg></div>
    <div class="measure" style="top:456px">Venting to flare<span class="count">0/0</span><span class="box"></span></div>
    <div class="measure" style="top:489px">reduced water injection<span class="count">0/0</span><span class="box"></span></div>
    <div class="measure on" style="top:522px">Reduced gaz injection<span class="count">18/18</span><span class="box"></span></div>
    <div class="measure on" style="top:555px">Compressor replacement<span class="count">7/28</span><span class="box"></span></div>
    <div class="measure" style="top:588px">Venting to production<span class="count">0/0</span><span class="box"></span></div>
    <div class="measure" style="top:621px">Drilling Improvements<span class="count">0/0</span><span class="box"></span></div>
    <div class="measure" style="top:654px">reduced water injection<span class="count">0/0</span><span class="box"></span></div>

    <div class="group" style="top:691px">Logisticts<span class="applied">0&nbsp; Applied</span><svg width="8" height="12" viewBox="0 0 8 12"><path d="M7 0v12L0 6z" fill="#fff"/></svg></div>
    <div class="group" style="top:732px">End of pipe measures<span class="applied">0&nbsp; Applied</span><svg width="8" height="12" viewBox="0 0 8 12"><path d="M7 0v12L0 6z" fill="#fff"/></svg></div>
    <div class="group" style="top:773px">Carbon offsets<span class="applied">0&nbsp; Applied</span><svg width="8" height="12" viewBox="0 0 8 12"><path d="M7 0v12L0 6z" fill="#fff"/></svg></div>
    <div class="group" style="top:814px">Company Structure<span class="applied">0&nbsp; Applied</span><svg width="8" height="12" viewBox="0 0 8 12"><path d="M7 0v12L0 6z" fill="#fff"/></svg></div>
  </aside>

  <section class="abs assets">
    <h2 class="abs panel-title" style="left:19px;top:15px">ASSETS</h2>
    <svg width="0" height="0" style="position:absolute">
      <defs>
        <symbol id="tick-ok" viewBox="0 0 14 14"><circle cx="7" cy="7" r="7" fill="#1aa37a"/><path d="M4 7.2l2 2 4-4.2" fill="none" stroke="#fff" stroke-width="1.6"/></symbol>
        <symbol id="tick-off" viewBox="0 0 14 14"><circle cx="7" cy="7" r="7" fill="#a2a9b0"/><path d="M4 7.2l2 2 4-4.2" fill="none" stroke="#fff" stroke-width="1.6"/></symbol>
      </defs>
    </svg>
    <div class="asset-row" style="top:53px"><span style="left:0">Asset name</span><span style="left:124px">data</span><span style="left:208px">additionals</span><span style="left:328px">date</span><svg class="tick" style="left:413px"><use href="#tick-ok"/></svg></div>
    <div class="asset-row" style="top:85px"><span style="left:0">Asset name</span><span style="left:124px">data</span><span style="left:208px">additionals</span><span style="left:328px">date</span><svg class="tick" style="left:413px"><use href="#tick-off"/></svg></div>
    <div class="asset-row" style="top:117px"><span style="left:0">Asset name</span><span style="left:124px">data</span><span style="left:208px">additionals</span><span style="left:328px">date</span><svg class="tick" style="left:413px"><use href="#tick-off"/></svg></div>
    <div class="asset-row" style="top:149px"><span style="left:0">Asset name</span><span style="left:124px">data</span><span style="left:208px">additionals</span><span style="left:328px">date</span><svg class="tick" style="left:413px"><use href="#tick-ok"/></svg></div>
    <div class="asset-row" style="top:181px"><span style="left:0">Asset name</span><span style="left:124px">data</span><span style="left:208px">additionals</span><span style="left:328px">date</span><svg class="tick" style="left:413px"><use href="#tick-ok"/></svg></div>
    <div class="asset-row" style="top:213px"><span style="left:0">Asset name</span><span style="left:124px">data</span><span style="left:208px">additionals</span><span style="left:328px">date</span><svg class="tick" style="left:413px"><use href="#tick-off"/></svg></div>

    <div class="abs adv-bar">Advanced Settings
      <svg style="position:absolute;right:36px" width="12" height="8" viewBox="0 0 12 8"><path d="M0 0h12L6 7z" fill="#0f4673"/></svg>
    </div>
    <div class="setting live" style="top:360px">Daily Monitoring<span class="state">Active</span><svg class="tick" style="left:413px"><use href="#tick-ok"/></svg></div>
    <div class="setting" style="top:393px">Compression advaced configuration<span class="state">inactive</span><svg class="tick" style="left:413px"><use href="#tick-off"/></svg></div>
    <div class="setting" style="top:426px">Advanced Recast<span class="state">inactive</span><svg class="tick" style="left:413px"><use href="#tick-off"/></svg></div>
    <div class="setting" style="top:459px">Compressor failure safty<span class="state">inactive</span><svg class="tick" style="left:413px"><use href="#tick-off"/></svg></div>
    <div class="setting live" style="top:492px">Activated advanced setting<span class="state">Active</span><svg class="tick" style="left:413px"><use href="#tick-ok"/></svg></div>
    <div class="setting" style="top:525px">This is an inactive one<span class="state">inactive</span><svg class="tick" style="left:413px"><use href="#tick-off"/></svg></div>
  </section>

  <section class="abs sim">
    <svg class="chart" width="589" height="595" viewBox="929 194 589 595">
      <rect x="1008" y="298" width="468" height="428" fill="#f8fbfe"/>
      <rect x="1075" y="298" width="66" height="428" fill="var(--band)"/>
      <rect x="1208" y="298" width="66" height="428" fill="var(--band)"/>
      <rect x="1342" y="298" width="66" height="428" fill="var(--band)"/>
      <line x1="997" y1="726" x2="1487" y2="726" stroke="#d3dae2"/>
      <text class="axis-label" x="971" y="310">20</text>
      <text class="axis-label" x="971" y="415">15</text>
      <text class="axis-label" x="971" y="520">10</text>
      <text class="axis-label" x="971" y="625">5</text>
      <text class="axis-label" x="971" y="730">0</text>
      <g class="axis-label" text-anchor="middle">
        <text x="1072" y="748">2022</text><text x="1140" y="748">2023</text><text x="1208" y="748">2024</text><text x="1275" y="748">2025</text><text x="1343" y="748">2026</text><text x="1411" y="748">2027</text><text x="1478" y="748">2027</text>
      </g>
      <g fill="none" stroke-width="3" stroke-linecap="round">
        <path stroke="var(--red)" d="M1008,516 C1040,460 1070,435 1100,434 C1140,432 1160,430 1200,408 C1240,392 1265,395 1285,410 C1310,430 1330,425 1360,400 C1400,370 1430,365 1462,368"/>
        <path stroke="var(--gold)" d="M1008,516 C1050,480 1090,450 1120,458 C1160,468 1180,515 1215,510 C1250,505 1290,475 1340,475 C1390,475 1420,488 1465,486"/>
        <path stroke="var(--purple)" d="M1008,516 C1040,495 1070,478 1095,492 C1130,512 1150,580 1190,575 C1230,568 1260,545 1300,535 C1340,528 1350,530 1380,510 C1410,490 1440,460 1465,456"/>
        <path stroke="var(--teal)" d="M1008,516 C1040,490 1080,460 1110,472 C1150,490 1200,580 1245,595 C1280,605 1300,620 1330,632 C1370,645 1380,625 1420,665 C1445,690 1455,700 1470,697"/>
      </g>
    </svg>
    <h2 class="abs panel-title" style="left:23px;top:21px">SIMULATION</h2>
    <div class="view-btn on" style="left:434px"><svg width="18" height="16" viewBox="0 0 18 16"><rect x="1" y="1" width="16" height="14" rx="2" fill="none" stroke="#fff" stroke-width="1.8"/><path d="M3 12l4-5 3 3 5-6v9H3z" fill="#fff"/></svg></div>
    <div class="view-btn" style="left:478px"><svg width="16" height="16" viewBox="0 0 16 16"><path d="M7 1a7 7 0 1 0 8 8H7z" fill="#0f4673"/><path d="M9 0v7h7A7 7 0 0 0 9 0z" fill="#0f4673"/></svg></div>
    <div class="view-btn" style="left:522px"><svg width="14" height="14" viewBox="0 0 14 14"><rect x="1" y="6" width="3" height="8" fill="#0f4673"/><rect x="5.5" y="1" width="3" height="13" fill="#0f4673"/><rect x="10" y="8" width="3" height="6" fill="#0f4673"/></svg></div>
    <div class="legend">
      <span><i style="background:var(--purple)"></i>Accumulated Effect</span>
      <span><i style="background:var(--gold)"></i>Second Strategy</span>
      <span><i style="background:var(--red)"></i>No Measures</span>
      <span><i style="background:var(--teal)"></i>Goal</span>
    </div>
  </section>

  <section class="abs timeline">
    <span class="year" style="left:37px">2022</span><span class="year" style="left:121px">2023</span><span class="year" style="left:205px">2024</span><span class="year" style="left:289px">2025</span><span class="year" style="left:373px">2026</span><span class="year" style="left:457px">2027</span><span class="year" style="left:540px">2027</span><span class="year" style="left:623px">2029</span><span class="year" style="left:707px">2030</span><span class="year" style="left:790px">2031</span><span class="year" style="left:873px">2032</span><span class="year" style="left:957px">2033</span><span class="year" style="left:1042px">2034</span>
    <span class="gridline" style="left:37px"></span><span class="gridline" style="left:121px"></span><span class="gridline" style="left:205px"></span><span class="gridline" style="left:289px"></span><span class="gridline" style="left:373px"></span><span class="gridline" style="left:457px"></span><span class="gridline" style="left:540px"></span><span class="gridline" style="left:623px"></span><span class="gridline" style="left:707px"></span><span class="gridline" style="left:790px"></span><span class="gridline" style="left:873px"></span><span class="gridline" style="left:957px"></span><span class="gridline" style="left:1042px"></span>

    <div class="plan gold" style="left:36px;top:187px;width:380px;top:36px">Compressor replacement<span class="modify">Modify <b></b></span></div>
    <div class="plan gold" style="left:541px;top:36px;width:334px">Compressor replacement<span class="modify">Modify <b></b></span></div>
    <div class="plan purple" style="left:122px;top:86px;width:334px;padding-left:24px">Biodiesel Enery Carrier<span class="modify">Modify <b></b></span></div>
    <div class="plan teal" style="left:373px;top:136px;width:334px">Biodiesel Enery Carrier<span class="modify">Modify <b></b></span></div>

    <div class="abs switch">
      <div class="pick">Measures View
        <svg width="12" height="12" viewBox="0 0 12 12"><rect x="0" y="0" width="5" height="5" fill="#0f4673"/><rect x="7" y="0" width="5" height="5" fill="#0f4673"/><rect x="0" y="7" width="5" height="5" fill="#0f4673"/></svg>
      </div>
      <div class="active">Assets View
        <svg width="12" height="12" viewBox="0 0 12 12"><rect x="0" y="1" width="12" height="10" rx="2" fill="#fff"/><rect x="2" y="5" width="8" height="1.5" fill="#0f4673"/></svg>
      </div>
    </div>
  </section>

</div>
</div>
</body>
</html>
```